Business card for the interior shop
Mirel Interior Design
Simple
Lenka Vautrin-Koreneva
Interior designer
Brunnweg 17, 8045, Zurich Switzerland
mirel@mirel-design.com
All the contact details

```html
<!DOCTYPE html>
<html lang="en">
<head>
<meta charset="utf-8">
<title>Mirel Interior Design – Stationery Set</title>
<link rel="stylesheet" href="https://fonts.googleapis.com/css2?family=Open+Sans:wght@400;600&display=swap">
<style>
  :root {
    --bg: #f1f1f1;
    --paper: #ffffff;
    --paper-edge: #dcdcdc;
    --accent: #f2a51a;
    --ink: #2b2b2b;
    --muted: #7a7a7a;
    --card-dark: #0e0e0e;
    --card-ink: #e6e6e6;
    --rule-dark: #3a3a3a;
  }
  * { box-sizing: border-box; margin: 0; padding: 0; }
  html, body { width: 1200px; height: 681px; overflow: hidden; }
  body {
    background: var(--bg);
    font-family: "Open Sans", Arial, sans-serif;
    color: var(--ink);
    position: relative;
  }
  .sheet {
    position: absolute;
    background: var(--paper);
    border: 1px solid var(--paper-edge);
  }

  /* Name block: plain square + company name, one weight, one colour */
  .brand {
    position: absolute;
    display: flex;
    align-items: center;
    gap: 0.45em;
    line-height: 1;
    white-space: nowrap;
  }
  .brand__mark {
    width: 0.8em;
    height: 0.8em;
    background: var(--accent);
    flex: none;
  }
  .brand__name {
    font-weight: 600;
    color: var(--ink);
  }

  /* Footer bands */
  .bands { position: absolute; left: 0; right: 0; }
  .bands__accent { height: 4px; background: var(--accent); }
  .bands__dark { height: 2px; background: var(--rule-dark); margin-top: 2px; }

  .contact {
    position: absolute;
    font-size: 7px;
    font-weight: 600;
    line-height: 1.5;
    color: var(--ink);
    white-space: nowrap;
  }

  /* Envelope front */
  .envelope-front { left: 60px; top: 96px; width: 492px; height: 216px; }
  .envelope-front .brand { left: 14px; top: 22px; font-size: 18px; }
  .envelope-front .bands { top: 163px; }
  .envelope-front .contact { left: 14px; top: 180px; }

  /* Envelope back */
  .envelope-back { left: 60px; top: 360px; width: 492px; height: 216px; }
  .envelope-back .flap { position: absolute; left: 0; top: 0; width: 100%; height: 70px; }
  .envelope-back .brand { left: 50%; top: 92px; transform: translateX(-50%); font-size: 15px; }

  /* Letterhead */
  .letterhead { left: 619px; top: 48px; width: 444px; height: 581px; }
  .letterhead .brand { left: 16px; top: 26px; font-size: 20px; }
  .letterhead .bands { top: 528px; }
  .letterhead .contact { left: 16px; top: 545px; }

  /* Business cards */
  .card {
    position: absolute;
    left: 967px;
    width: 180px;
    height: 104px;
    background: var(--card-dark);
    color: var(--card-ink);
  }
  .card--front { top: 137px; }
  .card--back { top: 268px; }
  .card .brand__name { color: var(--card-ink); }

  .card--front .brand { left: 8px; top: 12px; font-size: 8px; }
  .card__person {
    position: absolute; left: 100px; top: 10px;
    font-size: 5px; line-height: 1.5;
  }
  .card__person strong { font-weight: 600; display: block; }
  .card .bands { top: 50px; }
  .card .bands__accent { height: 2px; }
  .card .bands__dark { height: 1px; background: #6a6a6a; }
  .card__contact {
    position: absolute; left: 8px; top: 60px;
    font-size: 4.6px; line-height: 1.55; color: var(--card-ink);
    white-space: nowrap;
  }

  .card--back .brand { left: 50%; top: 50%; transform: translate(-50%, -50%); font-size: 10px; }
</style>
</head>
<body>

  <section class="sheet envelope-front" aria-label="Envelope front">
    <div class="brand">
      <span class="brand__mark"></span>
      <span class="brand__name">Mirel Interior Design</span>
    </div>
    <div class="bands"><div class="bands__accent"></div><div class="bands__dark"></div></div>
    <p class="contact">
      Brunnweg 17 | 8045, Zurich | Switzerland<br>
      Phone: +41 (0)44 555 01 23 | +41 (0)79 555 04 56 | Email: mirel@mirel-design.com
    </p>
  </section>

  <section class="sheet envelope-back" aria-label="Envelope back">
    <svg class="flap" viewBox="0 0 492 70" preserveAspectRatio="none" aria-hidden="true">
      <polyline points="0,0 36,58 456,58 492,0" fill="none" stroke="#9a9a9a" stroke-width="1"/>
    </svg>
    <div class="brand">
      <span class="brand__mark"></span>
      <span class="brand__name">Mirel Interior Design</span>
    </div>
  </section>

  <section class="sheet letterhead" aria-label="Letterhead">
    <div class="brand">
      <span class="brand__mark"></span>
      <span class="brand__name">Mirel Interior Design</span>
    </div>
    <div class="bands"><div class="bands__accent"></div><div class="bands__dark"></div></div>
    <p class="contact">
      Brunnweg 17 | 8045, Zurich | Switzerland<br>
      Phone: +41 (0)44 555 01 23 | +41 (0)79 555 04 56 | Email: mirel@mirel-design.com
    </p>
  </section>

  <section class="card card--front" aria-label="Business card front">
    <div class="brand">
      <span class="brand__mark"></span>
      <span class="brand__name">Mirel Interior Design</span>
    </div>
    <p class="card__person">
      <strong>Lenka Vautrin-Koreneva</strong>
      Interior designer
    </p>
    <div class="bands"><div class="bands__accent"></div><div class="bands__dark"></div></div>
    <p class="card__contact">
      Brunnweg 17, 8045, Zurich Switzerland<br>
      Phone: +41 (0)44 555 01 23 | +41 (0)79 555 04 56<br>
      Email: mirel@mirel-design.com
    </p>
  </section>

  <section class="card card--back" aria-label="Business card back">
    <div class="brand">
      <span class="brand__mark"></span>
      <span class="brand__name">Mirel Interior Design</span>
    </div>
  </section>

</body>
</html>
```